Card and board game developer website, small e-commerce site

We are designing a website for Copper Lantern Otter Works. I need a homepage and a typical inside page designed.
The website navigation will be:
Home (where we'll introduce the games and the website)
Our Games (drops open into the two games)
Griffins of Morvale Keep
Tidecraft
Order Now
About Us
Contact
The header of the website will include the logo, the navigation and a link to a facebook page. The header will also include a cart icon and a link to My Account.
Then on the homepage I suggest we include a row for each game:
Griffins of Morvale Keep
This row will include a photo (or maybe a series of photos that animate into each other) and quick info about the game plus two buttons: Info and Photos (which will go to the detail page with the photo gallery), and Order Now (which will take you to the product for ordering).
Tidecraft
Your footer will contain a copyright note, plus links to:
Terms and conditions
Shipping and returns
FAQ
Contact
Account login
NOTE: the logo is the orange mokey. I've uploaded a brief with more information. The current website that we are redesigning is here https://www.copperlanternotter.example/
Please send me any questions that you have.
Target Market(s)
People interested in fun card and board games at home.
Number of Pages Required
Look and feel

```html
<!DOCTYPE html>
<html lang="en">
<head>
<meta charset="utf-8">
<title>Copper Lantern Otter Works — Home</title>
<link rel="stylesheet" href="https://fonts.googleapis.com/css2?family=DM+Serif+Display&family=Inter:wght@400;500;600&display=swap">
<style>
  :root {
    --orange: #f2872a;
    --orange-soft: #f4a46a;
    --ink: #151515;
    --muted: #6a6a6a;
    --paper: #ffffff;
    --peach-top: #fbe9da;
    --peach-bottom: #fdf4ec;
    --line: #ece6e0;
    --serif: "DM Serif Display", Georgia, serif;
    --sans: "Inter", Arial, sans-serif;
  }
  * { box-sizing: border-box; margin: 0; padding: 0; }
  html, body { width: 1200px; height: 902px; overflow: hidden; }
  body { background: var(--orange); font-family: var(--sans); color: var(--ink); position: relative; }
  a { text-decoration: none; }

  .site {
    position: absolute; left: 64px; top: 68px; width: 1072px; height: 762px;
    background: linear-gradient(180deg, var(--peach-top) 0%, var(--peach-bottom) 100%);
    overflow: hidden;
  }
  .site-header {
    position: absolute; left: 0; top: 0; width: 100%; height: 74px;
    background: var(--paper); border-bottom: 1px solid var(--line);
  }
  .brand {
    position: absolute; left: 163px; top: 22px; display: flex; align-items: center; gap: 6px;
    font-family: var(--serif); font-size: 13px; color: var(--orange); line-height: 1.1; width: 120px;
  }
  .brand-dot { width: 14px; height: 14px; border-radius: 50%; background: var(--orange); flex: none; }
  .nav a {
    position: absolute; top: 28px; font-size: 13.4px; color: var(--ink); line-height: 18px;
  }
  .nav .nav-order {
    top: 19px; left: 513px; width: 140px; height: 38px; border-radius: 19px;
    background: var(--orange); color: #fff; text-align: center; line-height: 38px;
    box-shadow: 0 3px 6px rgba(242,135,42,.35);
  }
  .cart-link {
    position: absolute; left: 978px; top: 23px; width: 28px; height: 28px; border-radius: 50%;
    border: 1px solid var(--orange); display: flex; align-items: center; justify-content: center;
  }

  .hero-title {
    position: absolute; left: 163px; top: 155px; font-family: var(--serif); font-weight: 400;
    font-size: 36px; line-height: 49px; width: 420px;
  }
  .hero-lead { position: absolute; left: 163px; top: 273px; font-size: 13.2px; font-weight: 500; }
  .hero-points { position: absolute; left: 163px; top: 308px; font-size: 10.4px; line-height: 13px; list-style: none; }
  .btn {
    position: absolute; height: 24px; border-radius: 12px; font-size: 10.5px; text-align: center;
    line-height: 22px;
  }
  .btn-fill { background: var(--orange-soft); color: #fff; border: 1px solid var(--orange-soft); }
  .btn-line { background: #fff; color: #555; border: 1px solid var(--orange-soft); }

  .panel { position: absolute; background: var(--paper); border: 1px solid var(--line); border-radius: 4px; }
  .feature { left: 133px; top: 439px; width: 566px; height: 264px; }
  .feature-title {
    position: absolute; left: 36px; top: 78px; font-family: var(--serif); font-weight: 400;
    font-size: 24px; line-height: 36px; width: 260px;
  }
  .feature-mark {
    position: absolute; left: 314px; top: 40px; width: 222px; height: 186px;
    display: flex; flex-direction: column; align-items: center; justify-content: center; gap: 12px;
  }
  .feature-mark .mark-circle { width: 96px; height: 96px; border-radius: 50%; background: var(--orange); }
  .feature-mark span { font-family: var(--serif); font-size: 18px; color: var(--orange); text-align: center; line-height: 1.15; }

  .product { left: 723px; width: 263px; height: 264px; }
  .product-photo { position: absolute; left: 19px; top: 17px; width: 185px; height: 156px; border-radius: 6px; }
  .fav {
    position: absolute; left: 165px; top: 6px; width: 16px; height: 16px; border-radius: 50%;
    background: #fff; border: 1px solid var(--orange-soft);
  }
  .thumb { position: absolute; left: 211px; width: 32px; height: 33px; }
  .product-head {
    position: absolute; left: 47px; top: 181px; width: 200px;
    display: flex; align-items: baseline; justify-content: space-between; gap: 6px;
  }
  .product-name { font-family: var(--serif); font-size: 12px; font-weight: 400; white-space: nowrap; }
  .product-price { font-size: 5.5px; color: var(--muted); white-space: nowrap; }
  .product-desc { position: absolute; left: 47px; top: 200px; width: 110px; font-size: 4.2px; line-height: 5px; color: #444; }
  .product .btn { top: 225px; height: 25px; line-height: 23px; font-weight: 500; }
  .btn-learn { left: 19px; width: 96px; background: #fff; color: #555; border: 1px solid var(--orange-soft); }
  .btn-cart { left: 129px; width: 114px; background: #fff; color: var(--orange); border: 1px solid var(--orange-soft);
    display: flex; align-items: center; justify-content: center; gap: 6px; }
</style>
</head>
<body>
<div class="site">
  <header class="site-header">
    <a class="brand" href="#"><span class="brand-dot"></span>Copper Lantern Otter Works</a>
    <nav class="nav">
      <a href="#" style="left:353px">Home</a>
      <a href="#" style="left:415px">Our Games</a>
      <a href="#" class="nav-order">Order Now</a>
      <a href="#" style="left:679px">About</a>
      <a href="#" style="left:742px">Contact</a>
    </nav>
    <a class="cart-link" href="#" aria-label="Cart">
      <svg width="14" height="14" viewBox="0 0 24 24" fill="none" stroke="#f2872a" stroke-width="1.8" stroke-linecap="round" stroke-linejoin="round"><path d="M2 3h3l2.5 12h11L21 7H6.5"/><circle cx="9" cy="19.5" r="1.3"/><circle cx="17" cy="19.5" r="1.3"/></svg>
    </a>
  </header>

  <section class="hero">
    <h1 class="hero-title">Welcome to Copper Lantern Otter Works</h1>
    <p class="hero-lead">Order Now and Embark on a Journey of Fun and Strategy!</p>
    <ul class="hero-points">
      <li>🪶 Immerse Yourself in the World of Griffins with "Griffins of Morvale Keep"</li>
      <li>🔥 Master the Tides in the Fast-Paced Card Game "Tidecraft"</li>
    </ul>
    <a class="btn btn-fill" href="#" style="left:163px;top:361px;width:94px">Explore Games</a>
    <a class="btn btn-line" href="#" style="left:276px;top:361px;width:95px">View Artist</a>
  </section>

  <section class="panel feature">
    <h2 class="feature-title">Unleash the Power of Play with Our Unique Board Games</h2>
    <div class="feature-mark"><div class="mark-circle"></div><span>Copper Lantern<br>Otter Works</span></div>
  </section>

  <article class="panel product" style="top:132px">
    <div class="product-photo" role="img" aria-label="Photo of the Griffins of Morvale Keep game box" style="background:linear-gradient(160deg,#d9d8de,#c9c6cf 55%,#b5a4a6)">
      <span class="fav"></span>
    </div>
    <div class="thumb" role="img" aria-label="Box cover artwork" style="top:22px;background:#3c6a48"></div>
    <div class="thumb" role="img" aria-label="Game board in play" style="top:60px;background:#7f9c77"></div>
    <div class="thumb" role="img" aria-label="Game cards and pieces" style="top:97px;background:#8a5b56"></div>
    <div class="thumb" role="img" aria-label="Close-up of a game piece" style="top:134px;background:#263424"></div>
    <div class="product-head">
      <h3 class="product-name">Griffins of Morvale Keep</h3>
      <span class="product-price">$54.95</span>
    </div>
    <p class="product-desc">Step into Morvale Keep, the first board game where every player is a griffin.</p>
    <a class="btn btn-learn" href="#">Learn More</a>
    <a class="btn btn-cart" href="#"><svg width="11" height="11" viewBox="0 0 24 24" fill="none" stroke="#f2872a" stroke-width="2" stroke-linecap="round" stroke-linejoin="round"><path d="M2 3h3l2.5 12h11L21 7H6.5"/><circle cx="9" cy="19.5" r="1.3"/><circle cx="17" cy="19.5" r="1.3"/></svg>Add to Cart</a>
  </article>

  <article class="panel product" style="top:439px">
    <div class="product-photo" role="img" aria-label="Photo of the Tidecraft card deck box" style="background:linear-gradient(90deg,#e2e0de 0%,#6a4a36 40%,#4a3528 60%,#e2e0de 100%)">
      <span class="fav"></span>
    </div>
    <div class="thumb" role="img" aria-label="Card artwork" style="top:22px;background:#b5532a"></div>
    <div class="thumb" role="img" aria-label="Cards laid out on a table" style="top:60px;background:#a38561"></div>
    <div class="thumb" role="img" aria-label="Hand of cards" style="top:97px;background:#c9b99a"></div>
    <div class="thumb" role="img" aria-label="Deck box front" style="top:134px;background:#4a3528"></div>
    <div class="product-head">
      <h3 class="product-name">Tidecraft</h3>
      <span class="product-price">$14.95</span>
    </div>
    <p class="product-desc" style="width:104px">Welcome to Tidecraft, a fast-paced card game of strategy and chance.</p>
    <a class="btn btn-learn" href="#">Learn More</a>
    <a class="btn btn-cart" href="#"><svg width="11" height="11" viewBox="0 0 24 24" fill="none" stroke="#f2872a" stroke-width="2" stroke-linecap="round" stroke-linejoin="round"><path d="M2 3h3l2.5 12h11L21 7H6.5"/><circle cx="9" cy="19.5" r="1.3"/><circle cx="17" cy="19.5" r="1.3"/></svg>Add to Cart</a>
  </article>
</div>
</body>
</html>
```